Construction Company Facebook Banner

We are a small residential building company, building mostly new homes, renovations, extensions. our social media needs an uplift to look more professional.
I have no photos I wish to use in the banner as of yet however I have included the company logo, and the business card design which has some details.
I would like something simple but professional.
The banner does not need to have email, phone number, services provided etc. all of this is available on the facebook page itself. Something simple and clean please.
Industry/Entity Type
Construction
Requirements
Should not have
- Images of people, QR Code

```html
<!DOCTYPE html>
<html lang="en">
<head>
<meta charset="utf-8">
<title>Ridgeline Homes – Cover Banner</title>
<link href="https://fonts.googleapis.com/css2?family=Montserrat:wght@700&family=Exo+2:wght@300&display=swap" rel="stylesheet">
<style>
  :root {
    --page-bg: #e9ebee;
    --banner-dark: #272727;
    --banner-deep: #070707;
    --text-light: #ffffff;
    --accent-green: #2db84b;
  }
  html, body {
    margin: 0;
    padding: 0;
    width: 1200px;
    height: 588px;
    overflow: hidden;
    background: var(--page-bg);
  }
  .cover-banner {
    position: absolute;
    left: 0;
    top: 72px;
    width: 1200px;
    height: 444px;
    background: linear-gradient(100deg, var(--banner-dark) 0%, var(--banner-dark) 55%, #161616 78%, var(--banner-deep) 100%);
    border-radius: 0 0 8px 8px;
    overflow: hidden;
  }
  .backdrop-shape {
    position: absolute;
    left: 620px;
    top: 0;
    width: 580px;
    height: 444px;
    background: linear-gradient(120deg, rgba(40,40,40,0) 0%, rgba(22,22,22,0.8) 55%, rgba(0,0,0,0.9) 100%);
  }
  .brand {
    position: absolute;
    left: 61px;
    top: 50px;
    display: flex;
    align-items: center;
    gap: 22px;
  }
  .brand-square {
    width: 62px;
    height: 62px;
    background: var(--accent-green);
  }
  .brand-name {
    font-family: "Montserrat", sans-serif;
    font-weight: 700;
    color: var(--text-light);
    line-height: 1;
    text-transform: uppercase;
  }
  .brand-name .line-main {
    display: block;
    font-size: 38px;
    letter-spacing: -0.5px;
  }
  .brand-name .line-sub {
    display: block;
    font-size: 19px;
    margin-top: 6px;
    letter-spacing: 0.2px;
  }
  .services {
    position: absolute;
    left: 61px;
    top: 162px;
    width: 577px;
    font-family: "Exo 2", sans-serif;
    font-weight: 300;
    font-size: 27px;
    line-height: 36.5px;
    color: var(--text-light);
  }
  .services .row {
    text-align: justify;
    text-align-last: justify;
    white-space: nowrap;
  }
  .dot {
    display: inline-block;
    width: 6px;
    height: 6px;
    border-radius: 50%;
    background: var(--accent-green);
    vertical-align: middle;
    margin: 0 2px;
  }
</style>
</head>
<body>
  <section class="cover-banner">
    <div class="backdrop-shape" role="img" aria-label="Dark abstract roofline backdrop"></div>

    <div class="brand">
      <div class="brand-square"></div>
      <div class="brand-name">
        <span class="line-main">Ridgeline Homes</span>
        <span class="line-sub">and Construction Pty Ltd</span>
      </div>
    </div>

    <div class="services">
      <div class="row">New Homes <span class="dot"></span> Extencions <span class="dot"></span> Renovations &amp;</div>
      <div class="row">Bathrooms <span class="dot"></span> Decking <span class="dot"></span> Carports <span class="dot"></span> Sheds</div>
      <div class="row">(Residential and Industrial) <span class="dot"></span> Carpentry</div>
      <div class="row">Fences Patios &amp; Pergolas <span class="dot"></span> Building Inspections</div>
    </div>
  </section>
</body>
</html>
```